Etiketten für Imkerei mit Spezialisierung auf Bio Lagenhonig
Zielgruppe
wiesentau.at - BioImkerei Lindorf
Kleine Nebenerwerbs Imkerei mit Spezialisierung auf Bio Lagenhonig (nähere Infos sind auf der Website nachzulesen)
Als weitere Produktlinie bieten wir Honig+ / Honig mit Zutaten wie Himbeer, Erdbeer, Haselnuss, Mohn, Ingwer, Thymian, usw an.
Zielgruppe: Personen die offen für die Vielfalt der Natur sind, gesunde und natürliche Lebensmittel lieben und die bereit sind die aufwändige, großteils manuelle, Arbeit entsprechend zu entlohnen.
Gesucht:
ÄNDERUNG: Da die Anforderung für das ausgesetzte Preisgeld offensichtlich zu komplex ist, reduziere ich die Anforderung auf Etiketten für die Produktserie Honig+, Gesamtkonzepte sind nicht erforderlich werden aber gerne angenommen.
ÜRSPRÜNGLICH:
Redesign der aktuellen Honigetiketten
Basisdesign für Lagenhonig und Honig+ das entsprechende Varianten zulässt.
Aufgabenstellung
Ich wünsche mir ein modernes, edles (oder Öko look) Design mit sehr guten Wiedererkennungswert das sich von gängigen Honigetiketten deutlich abhebt.
Das wiesentau Logo soll enthalten sein kann aber bei Bedarf angepasst werden (z.B. monocrome Verison)
Für Lagenhonig werden derzeit 400g und 100g Gläser mit hohem schwarzen DrehFix Decke und,
für Honig+ 250g und 100g mit hohem silbenen DrehFix Deckel verwendet. Beispiele sind im Webshop unter https://hofkorb.at/index.php/wiesentau ersichtilich.
Für das Ablaufdatum ist evtl. ein Feld für manuelle Stempelung vorzusehen.
Bitte die Sichtfeldregelung der EU Verpackungsverordnung einhalten.
Bisherige Etiketten hatten den Anspruch das diese auf guten Laserdruckern ausdruckbar waren - das ist jetzt nicht mehr zwingend notwendig (wäre für Kleinauflagen aber trotzdem vorteilhaft)

```html
<!DOCTYPE html>
<html lang="de">
<head>
<meta charset="utf-8">
<title>Bio Honig aus dem Kamptal – Etikett Honig+ Erdbeer</title>
<link rel="stylesheet" href="https://fonts.googleapis.com/css2?family=Arimo:wght@400;700&display=swap">
<style>
  :root {
    --canvas-bg: #f3f1ed;
    --band-black: #0c0c0c;
    --band-text: #f5f5f5;
    --panel-white: #ffffff;
    --ink: #161616;
    --organic-green: #86b847;
  }
  * { margin: 0; padding: 0; box-sizing: border-box; }
  html, body {
    width: 1200px;
    height: 1200px;
    overflow: hidden;
    background: var(--canvas-bg);
  }
  .canvas {
    position: relative;
    width: 1200px;
    height: 1200px;
    font-family: "Arimo", Arial, sans-serif;
    color: var(--ink);
  }
  .label {
    position: absolute;
    left: 50px;
    top: 341px;
    width: 1100px;
    height: 518px;
    background: var(--band-black);
  }
  .label__title {
    position: absolute;
    left: 77px;
    top: 38px;
    font-size: 40px;
    font-weight: 400;
    letter-spacing: 0.5px;
    color: var(--band-text);
  }
  .info-panel {
    position: absolute;
    left: 58px;
    top: 123px;
    width: 1004px;
    height: 378px;
    background: var(--panel-white);
  }
  .info-panel > * { position: absolute; white-space: nowrap; line-height: 1.15; }

  .product-name { left: 28px; top: 20px; font-size: 30px; }
  .product-origin { left: 28px; top: 56px; font-size: 22px; line-height: 33px; }
  .net-weight { left: 26px; top: 116px; font-size: 62px; }

  .organic-badge { left: 30px; top: 196px; width: 192px; height: 117px; }
  .cert-code { left: 250px; top: 238px; font-size: 22px; font-weight: 700; }
  .cert-origin { left: 250px; top: 288px; font-size: 21px; }
  .organic-note { left: 33px; top: 336px; font-size: 22px; }

  .ingredients { left: 460px; top: 18px; font-size: 22px; }
  .ingredients__second { left: 590px; top: 46px; font-size: 22px; }
  .ingredients__note { left: 590px; top: 73px; font-size: 19px; line-height: 24px; }

  .best-before { left: 390px; top: 160px; font-size: 23px; }
  .storage { left: 390px; top: 200px; font-size: 21px; }

  .producer { left: 650px; top: 244px; font-size: 23px; font-weight: 700; }
  .producer-address { left: 650px; top: 284px; font-size: 22px; line-height: 33px; text-align: left; }
</style>
</head>
<body>
<main class="canvas">
  <section class="label">
    <h1 class="label__title">Bio Honig aus dem Kamptal</h1>

    <div class="info-panel">
      <h2 class="product-name">Honigkomposition</h2>
      <p class="product-origin">mit österreichischen Blütenhonig<br>aus biologischer Bienenhaltung</p>
      <p class="net-weight">100g</p>

      <svg class="organic-badge" viewBox="0 0 192 117" role="img" aria-label="EU-Bio-Siegel">
        <rect x="0" y="0" width="150" height="117" fill="var(--organic-green)"/>
        <rect x="156" y="0" width="36" height="117" fill="var(--organic-green)"/>
      </svg>
      <p class="cert-code">AT-BIO-917</p>
      <p class="cert-origin">EU-Landwirtschaft</p>
      <p class="organic-note">*aus kontrolliert biologischer Landwirtschaft</p>

      <p class="ingredients">Zutaten: Blütenhonig* 95%</p>
      <p class="ingredients__second">Erdbeerpulver* 5%</p>
      <p class="ingredients__note">(gefriergetrocknet entspricht<br>45% Frischfruchtanteil)</p>

      <p class="best-before">Mindestens haltbar bis: 30.06.2017</p>
      <p class="storage">vor Wärme geschützt und trocken lagern</p>

      <p class="producer">BioImkerei Lindorf</p>
      <p class="producer-address">&nbsp;&nbsp;Wiesenweg 12<br>3571 Feldbach am Kamp<br>&nbsp;www.wiesentau.at</p>
    </div>
  </section>
</main>
</body>
</html>
```